Harborline Coverage (02)

We're designing a website to sell Medicare Supplements. Attached is the content we want to say and general layout, but please use your best knowledge to make it better. This platform is intentionally simplistic because this is reaching an older demographic, so it should be very straightforward, attention-grabbing and extremely user-friendly, while still appearing reliable and professional.
This should be a two-page web design. The homepage has information on Medicare supplements (script in image attached below) along with a button to input zip code. This triggers a window to pop up asking for personal information (will also be listed in attachment).
This brings you to the second page that lists out the medicare supplement companies and plans based on inputed information. We just want to see the design you have in mind, so it doesn't matter what information you put in this section. Feel free to reference/replicate the information in image 3 in the doc. There should be a section where you can filter results by company, premium price, or coverage plans.
Target Market(s)
Seniors, 65+
Industry/Entity Type
Insurance
Number of Pages Required
2 page
Look and feel
Each slider illustrates characteristics of the customer's brand and the style your logo design should communicate.

```html
<!DOCTYPE html>
<html lang="en">
<head>
<meta charset="utf-8">
<title>Harborline Coverage – Get a Quote</title>
<link href="https://fonts.googleapis.com/css2?family=Lato:ital,wght@0,400;0,700;0,900;1,400&family=Crimson+Text:ital@1&display=swap" rel="stylesheet">
<style>
:root{
  --navy:#1b2f5e;
  --navy-deep:#142347;
  --red:#e8344e;
  --ink:#2a2a2a;
  --grey-bg:#eeeeee;
  --white:#ffffff;
  --muted:#9aa0ab;
  --shade:rgba(8,14,32,.74);
}
*{margin:0;padding:0;box-sizing:border-box}
html,body{width:884px;height:1200px;overflow:hidden}
body{position:relative;font-family:'Lato',sans-serif;background:var(--navy-deep)}
.abs{position:absolute}

/* hero */
.hero{left:0;top:0;width:884px;height:463px;background:linear-gradient(100deg,#1d3263 0%,#243c70 55%,#3a4f7e 100%)}
.hero-photo{left:560px;top:60px;width:324px;height:403px;background:radial-gradient(ellipse at 50% 35%,#b8bcc6 0%,#6a7590 45%,rgba(36,60,112,0) 75%)}
.brand{left:63px;top:21px;font-size:16px;color:var(--white)}
.nav{right:64px;top:23px;display:flex;gap:20px;font-size:10px;color:var(--white)}
.nav .active{color:var(--red)}
.hero-title{left:63px;top:155px;font-size:35px;font-weight:900;color:var(--white);letter-spacing:.3px}
.hero-sub{left:63px;top:204px;width:440px;font-family:'Crimson Text',serif;font-style:italic;font-size:21px;line-height:22px;color:var(--white)}
.read-more{left:63px;top:275px;width:92px;height:29px;border-radius:15px;background:var(--red);color:var(--white);font-size:8px;display:flex;align-items:center;justify-content:center}
.zip{left:63px;top:379px;width:200px;height:51px;background:var(--white);padding:6px 6px}
.zip small{display:block;font-size:10px;color:#555}
.zip span{font-size:17px;font-style:italic;color:var(--navy)}

/* plans section */
.plans{left:0;top:463px;width:884px;height:435px;background:var(--grey-bg)}
.frame-outer{left:63px;top:500px;width:180px;height:335px;border:3px solid var(--navy)}
.frame-photo{left:87px;top:523px;width:170px;height:338px;border:2px solid var(--red);background:linear-gradient(160deg,#8b8f98,#3c4150)}
.plans-title{left:700px;top:542px;font-size:23px;font-weight:900;color:var(--red)}
.plans-text{left:700px;top:588px;width:120px;font-size:11px;line-height:16px;color:#444}

/* costs section */
.costs-title{left:62px;top:950px;font-size:31px;font-weight:900;color:var(--white);line-height:32px}
.costs-title span{display:block;color:var(--red);font-size:24px}
.costs-text{left:63px;top:1028px;width:375px;font-size:11px;line-height:16px;color:var(--white)}
.bullet{left:63px;top:1150px;width:380px;font-size:10px;line-height:13px;color:var(--white);display:flex;gap:10px}
.bullet b{color:var(--red);font-weight:400}
.lab-frame{left:720px;top:937px;width:100px;height:263px;border:3px solid #c9ccd4;border-bottom:none}
.lab-photo{left:459px;top:961px;width:337px;height:239px;border:2px solid var(--red);border-bottom:none;background:radial-gradient(ellipse at 55% 40%,#c7ccd4 0%,#5a6376 50%,#243152 100%)}

.shade{left:0;top:0;width:884px;height:1200px;background:var(--shade)}

/* quote modal */
.modal{left:153px;top:238px;width:579px;height:723px;background:var(--white);padding:24px 18px 0}
.modal h2{font-size:28px;font-weight:700;color:var(--navy);margin-bottom:16px}
.modal h2 span{color:var(--red)}
.lead{font-size:17px;line-height:22px;color:var(--ink);margin-bottom:14px}
.intro{font-size:17px;line-height:23px;color:var(--ink);margin-bottom:42px}
.req{color:var(--red)}
.note,.field-label{font-size:18px;font-weight:700;color:var(--ink)}
.note{margin-bottom:28px}
.radio{display:flex;align-items:center;gap:12px;font-size:18px;font-weight:700;color:var(--ink);margin:0 0 17px 11px}
.radio i{width:19px;height:19px;border:2px solid var(--navy);border-radius:50%}
.gender{margin-bottom:10px}
.input{height:47px;border:2px solid var(--navy);border-radius:5px;font-size:14px;color:var(--muted);padding:0 11px;display:flex;align-items:center;box-shadow:0 2px 3px rgba(0,0,0,.15)}
.dob{width:234px;margin:8px 0 22px}
.section-label{font-size:18px;font-weight:700;color:var(--ink);margin-bottom:9px}
.row{display:flex;gap:14px}
.row .col{width:233px}
.row .field-label{font-size:15px}
.row .input{margin-top:6px}
.actions{display:flex;align-items:center;gap:12px;margin-top:17px}
.btn{width:163px;height:48px;background:var(--navy);border-radius:5px;color:var(--white);font-size:15px;font-weight:700;display:flex;align-items:center;justify-content:center;gap:16px;box-shadow:0 2px 4px rgba(0,0,0,.25)}
.cancel{font-size:15px;font-weight:700;color:var(--red)}
</style>
</head>
<body>
<div class="abs hero"></div>
<div class="abs hero-photo" role="img" aria-label="Smiling advisor in office setting"></div>
<div class="abs brand">Harborline Coverage</div>
<nav class="abs nav"><span class="active">Home</span><span>About</span><span>Features</span><span>Product</span><span>Reviews</span><span>Faq</span><span>Contact</span></nav>
<h1 class="abs hero-title">HARBORLINE COVERAGE</h1>
<p class="abs hero-sub">Be confident in choosing the Medicare Supplement plan that’s right for you</p>
<div class="abs read-more">READ MORE</div>
<div class="abs zip"><small>Zip Code</small><span>Enter Zip Code</span></div>

<div class="abs plans"></div>
<div class="abs frame-outer"></div>
<div class="abs frame-photo" role="img" aria-label="Doctor consulting with a patient"></div>
<div class="abs plans-title">PLAN?</div>
<p class="abs plans-text">Each plan offers a different level of coverage, the same with every company and they always cover plans must 365 days<br><br>and treatments.</p>

<h2 class="abs costs-title">MEDICARE SUPPLEMENT<span>INSURANCE PLAN COSTS</span></h2>
<p class="abs costs-text">Although private insurance companies are required to offer the same basic benefits for each lettered plan, they do have the ability to charge different premiums. You might want to shop around to find a Medicare Supplement insurance plan that may fit your medical and financial needs. Insurance companies may price their plan premiums in any of the following ways:</p>
<div class="abs bullet"><svg width="12" height="12" viewBox="0 0 12 12"><path d="M3 1l5 5-5 5" fill="none" stroke="#fff" stroke-width="2"/></svg><p><b>Community no-age-rated:</b> These Medicare Supplement insurance plans charge premiums that are the same across the board, regardless of age.</p></div>
<div class="abs lab-frame"></div>
<div class="abs lab-photo" role="img" aria-label="Lab researcher using a microscope"></div>

<div class="abs shade"></div>

<section class="abs modal">
  <h2><span>Get a</span> Quote</h2>
  <p class="lead">To figure out what your monthly premium would, be enter your<br>&nbsp;genderand date of birth</p>
  <p class="intro">ontrary to popular belief, Lorem Ipsum is not simply random text. It has roots in a piece of classical Latin literature from 45 BC, making it over 2000 years old.</p>
  <p class="note"><span class="req">*</span> Required</p>
  <div class="gender">
    <p class="field-label" style="margin-bottom:12px"><span class="req">*</span> Gender</p>
    <div class="radio"><i></i>Male</div>
    <div class="radio"><i></i>Female</div>
  </div>
  <p class="field-label">Date of birth <span class="req">*</span></p>
  <div class="input dob">mm/dd/yyyy</div>
  <p class="section-label">Hospital insurance (Part A)</p>
  <div class="row">
    <div class="col"><p class="field-label">Part A Month <span class="req">*</span></p><div class="input">Date</div></div>
    <div class="col"><p class="field-label">Part A Year <span class="req">*</span></p><div class="input">Year</div></div>
  </div>
  <div class="actions">
    <div class="btn">Compare Rates <svg width="12" height="16" viewBox="0 0 12 16"><path d="M2 2l6 6-6 6" fill="none" stroke="#fff" stroke-width="3"/></svg></div>
    <span class="cancel">Cancel</span>
  </div>
</section>
</body>
</html>
```